Offshore Energy Projects Management Consultancy needs a business card design

Logo available. We provide teams to deliver engineering consultancy, project management and delivery teams mainly in the offshore renewables sector. The company is all about bringing the right people to a project to deliver the scope.

The business card will be used for all staff.

The business card should be quite simple, vibrant and uncluttered but convey experience, enthusiasm and integration.

Target Market(s)

Energy Project Developers and Tier 1 construction companies

Contact Information for Business Card

Logo should be on the back of the card. I'm happy for the designer to play with the colour of the logo and background colour.

Front of the card should convey all the must have information in a clear and professional manner but without being overly traditional.

Colors

Designer to choose colors to be used in the design.

Requirements
Must have
• Land Line Tel Number, Mobile Tel Number, Email, business address, web address.

```html
<!DOCTYPE html>
<html lang="en">
<head>
<meta charset="utf-8">
<title>Tidewell Project Partners – Business Card</title>
<link href="https://fonts.googleapis.com/css2?family=Arimo:wght@400;700&display=swap" rel="stylesheet">
<style>
  :root {
    --bg: #efefef;
    --card: #ffffff;
    --ink-grey: #6f6f72;
    --ink-blue: #1f78c1;
    --tint: #e8f1f9;
    --sky-top: #2f86c8;
    --sky-mid: #6fb6e0;
    --sea: #b9cfdc;
    --white: #ffffff;
  }
  * { box-sizing: border-box; margin: 0; padding: 0; }
  html, body { width: 1200px; height: 864px; overflow: hidden; }
  body {
    background: var(--bg);
    font-family: "Arimo", Arial, sans-serif;
    position: relative;
  }
  .card {
    position: absolute;
    top: 257px;
    width: 540px;
    height: 350px;
    border-radius: 2px;
    box-shadow: 0 8px 24px rgba(0,0,0,0.12);
    overflow: hidden;
  }
  .card--back { left: 40px; }
  .card--front { left: 620px; background: var(--card); }

  /* Back */
  .back-scene {
    position: absolute; inset: 0;
    background: linear-gradient(180deg, var(--sky-top) 0%, var(--sky-mid) 55%, var(--sea) 100%);
  }
  .socials {
    position: absolute; top: 40px; left: 0; right: 0;
    display: flex; justify-content: center; gap: 26px;
    color: var(--white); font-size: 13px;
  }
  .socials__item { display: flex; align-items: center; gap: 7px; }
  .socials__dot { width: 12px; height: 12px; border-radius: 50%; background: var(--white); }
  .brand {
    position: absolute; top: 140px; left: 0; right: 0;
    text-align: center;
    color: var(--white);
    font-weight: 700; font-size: 30px; letter-spacing: 1px;
    text-transform: uppercase;
  }
  .brand__sub {
    display: block; margin-top: 8px;
    font-weight: 400; font-size: 13px; letter-spacing: 8px;
  }

  /* Front */
  .front-band {
    position: absolute; left: 0; right: 0; top: 170px; height: 120px;
    background: var(--tint);
  }
  .identity {
    position: absolute; top: 110px; right: 290px;
    text-align: right;
  }
  .identity__name {
    color: var(--ink-grey); font-weight: 700; font-size: 24px; line-height: 1.05;
  }
  .identity__title {
    color: var(--ink-blue); font-size: 17px; margin-top: 4px;
  }
  .divider {
    position: absolute; top: 108px; left: 266px;
    width: 2px; height: 92px; background: var(--ink-blue);
  }
  .contacts {
    position: absolute; top: 118px; left: 284px;
    list-style: none; font-size: 14.5px; line-height: 1.6; color: var(--ink-grey);
  }
  .contacts__label { color: var(--ink-blue); font-weight: 700; display: inline-block; width: 22px; }
  .address {
    position: absolute; left: 30px; bottom: 26px;
    font-size: 15px; color: var(--ink-grey);
  }
</style>
</head>
<body>
  <section class="card card--back" aria-label="Card back">
    <div class="back-scene" role="img" aria-label="Photograph of offshore wind turbines at sea under a blue sky"></div>
    <ul class="socials">
      <li class="socials__item"><span class="socials__dot"></span>@tidewellpp</li>
      <li class="socials__item"><span class="socials__dot"></span>/tidewell.pp</li>
      <li class="socials__item"><span class="socials__dot"></span>company/tidewell</li>
    </ul>
    <p class="brand">Tidewell<span class="brand__sub">Project Partners</span></p>
  </section>

  <section class="card card--front" aria-label="Card front">
    <div class="front-band"></div>
    <div class="identity">
      <p class="identity__name">Name<br>Surname</p>
      <p class="identity__title">Job Title</p>
    </div>
    <div class="divider"></div>
    <ul class="contacts">
      <li><span class="contacts__label">T:</span>+44(0) 1632 960 418</li>
      <li><span class="contacts__label">M:</span>+44(0) 7700 900 275</li>
      <li><span class="contacts__label">E:</span>name.surname@tidewell.example</li>
    </ul>
    <p class="address">Harbourline House, 12 Quay Road, Northport, NP4 2QT</p>
  </section>
</body>
</html>
```